Marlowvex Website Concept

We would like a one page website. Please refer to the attached files for more information.

Please reference file attachment version 1.1.

```html
<!DOCTYPE html>
<html lang="en">
<head>
<meta charset="utf-8">
<title>Marlowvex Security</title>
<link rel="stylesheet" href="https://fonts.googleapis.com/css2?family=Oswald:wght@400;500&family=Arimo:ital,wght@0,400;0,700;1,400&display=swap">
<style>
:root{
  --navy:#1c3d60;
  --navy-deep:#142c47;
  --ink:#2a2a2a;
  --muted:#6b6b6b;
  --page:#ffffff;
  --section-grey:#f0f0f0;
  --form-grey:#dedede;
  --field:#6d7f90;
  --dark:#16191d;
  --dark-2:#1e2328;
  --line:#9aa3ab;
  --link-blue:#2b5a8a;
}
*{box-sizing:border-box;margin:0;padding:0}
html,body{width:1200px;height:2769px;overflow:hidden;background:var(--page)}
body{position:relative;font-family:"Arimo",Arial,sans-serif;color:var(--ink)}
.abs{position:absolute}
.heading{font-family:"Oswald",sans-serif;font-weight:500;color:var(--navy)}

/* header */
.site-header{left:0;top:0;width:1200px;height:138px;background:#fff}
.brand{left:92px;top:38px;display:flex;align-items:center;gap:16px}
.brand-dot{width:60px;height:60px;border-radius:50%;background:var(--navy)}
.brand-name{font-family:"Oswald",sans-serif;font-weight:500;font-size:44px;color:var(--navy);letter-spacing:1px}
.social{top:18px;width:44px;height:44px;border-radius:50%;background:#a8a8a8}
.nav{top:84px;display:flex;gap:52px;left:640px;font-size:17px;color:var(--navy)}

.hero{left:0;top:138px;width:1200px;height:487px;
  background:linear-gradient(120deg,#eef0f2 0%,#d9dde1 35%,#9aa7b3 60%,#3e5368 85%,#24364a 100%)}

/* section titles */
.title-center{top:652px;width:1200px;text-align:center;font-size:38px}
.divider{height:2px;background:#b9c0c7}
.divider::before,.divider::after{content:"";position:absolute;top:-4px;width:10px;height:10px;border-radius:50%;background:var(--navy)}
.divider::before{left:-4px}.divider::after{right:-4px}

.card{top:748px;width:323px;height:347px;background:#fff;border:1px solid #dcdcdc}
.card-photo{position:absolute;inset:0;height:347px}
.card-band{position:absolute;left:0;bottom:0;width:100%;height:95px;background:rgba(255,255,255,.82);text-align:center}
.card-title{font-family:"Oswald",sans-serif;font-size:26px;color:var(--navy);margin-top:8px}
.card-btn{display:inline-block;margin-top:8px;padding:5px 22px;border:2px solid var(--navy);border-radius:14px;font-size:14px;font-weight:700;color:var(--navy);background:#fff}

.intro{left:130px;top:1120px;width:940px;text-align:center;font-size:17px;line-height:28px;color:var(--muted)}
.intro b{color:var(--link-blue)}

/* testimonial */
.testimonial{left:0;top:1271px;width:1200px;height:246px;background:linear-gradient(90deg,#0f1216,#23292f 60%,#14181c)}
.t-photo{left:123px;top:1317px;width:160px;height:154px;border:4px solid #fff;background:linear-gradient(160deg,#c9d3dc,#6e8296)}
.t-quote{left:302px;top:1300px;font-size:64px;color:#fff;font-family:Georgia,serif}
.t-text{left:357px;top:1325px;width:726px;font-style:italic;font-size:17px;line-height:25px;color:#c3d4e6}
.t-author{left:357px;top:1455px;font-style:italic;font-size:17px;color:#fff}
.t-more{left:1000px;top:1455px;font-size:18px;color:#fff}

/* services */
.services-bg{left:0;top:1517px;width:1200px;height:775px;background:var(--section-grey)}
.sec-title{font-size:38px}
.svc-icon{width:108px;height:108px;border-radius:50%;background:var(--navy);display:flex;align-items:center;justify-content:center}
.svc-name{font-size:17px;color:var(--navy)}
.svc-desc{font-size:15px;line-height:22px;color:var(--muted);width:150px}

.form-panel{left:794px;top:1640px;width:298px;height:622px;background:var(--form-grey)}
.field{left:818px;width:259px;height:36px;background:var(--field);color:#fff;font-size:14px;padding:10px 12px}
.send{left:818px;top:2200px;width:130px;height:40px;background:var(--navy-deep);color:#fff;font-size:15px;text-align:center;line-height:40px}

/* dark footer */
.footer-dark{left:0;top:2292px;width:1200px;height:422px;background:linear-gradient(90deg,#0d1014,#1c2126 50%,#101317)}
.f-title{font-family:"Oswald",sans-serif;font-size:25px;color:#fff}
.f-rule{height:1px;background:#5c6670}
.review{left:117px;top:2392px;width:290px;font-size:13px;line-height:19px;color:#c0c6cc}
.review-name{left:117px;top:2614px;font-size:14px;color:#fff;line-height:20px}
.pager{top:2668px;height:6px;background:#5c6670}
.thumb{width:124px;height:122px;background:linear-gradient(170deg,#e6e3de,#6b7684)}
.news-box{left:815px;top:2391px;width:262px;height:255px;background:var(--navy-deep)}
.news-text{left:840px;top:2420px;width:215px;font-size:14px;line-height:20px;color:#b8c6d6}
.news-input{left:840px;top:2492px;width:210px;height:40px;background:#fff;color:#999;font-size:14px;padding:11px 12px}
.news-btn{left:840px;top:2584px;width:210px;height:40px;background:#2b5176;color:#fff;font-size:15px;text-align:center;line-height:40px;border:1px solid #5c7fa2}

.footer-bar{left:0;top:2714px;width:1200px;height:55px;background:#f1f1f1;font-size:14px;color:#666}
</style>
</head>
<body>

<header class="abs site-header">
  <div class="abs brand"><span class="brand-dot"></span><span class="brand-name">Marlowvex</span></div>
  <span class="abs social" style="left:950px" aria-label="Social link"></span>
  <span class="abs social" style="left:1003px" aria-label="Social link"></span>
  <span class="abs social" style="left:1056px" aria-label="Social link"></span>
  <nav class="abs nav"><span>Company Description</span><span>Service Offerings</span><span>Contact Us</span></nav>
</header>

<div class="abs hero" role="img" aria-label="Photo of a hand signing a document beside a calculator and coins"></div>

<h2 class="abs heading title-center">Company Description</h2>
<div class="abs divider" style="left:98px;top:719px;width:997px"></div>

<div class="abs card" style="left:98px">
  <div class="card-photo" role="img" aria-label="Photo of a boardroom interior" style="background:linear-gradient(180deg,#d8d3cb,#8c8378)"></div>
  <div class="card-band"><div class="card-title">MARLOWVEX SECURITY</div><span class="card-btn">Read More</span></div>
</div>
<div class="abs card" style="left:440px">
  <div class="card-photo" role="img" aria-label="Photo of a team of business professionals" style="background:linear-gradient(180deg,#f2f2f2,#9aa0a8)"></div>
  <div class="card-band"><div class="card-title">FINANCIAL SERVICES</div><span class="card-btn">Read More</span></div>
</div>
<div class="abs card" style="left:778px">
  <div class="card-photo" role="img" aria-label="Photo of smiling business colleagues" style="background:linear-gradient(180deg,#eef0f3,#4f5b6a)"></div>
  <div class="card-band"><div class="card-title">OUR SERVICES</div><span class="card-btn">Read More</span></div>
</div>

<p class="abs intro"><b>Marlowvex Security</b>, LLC is a United States-based tier one security firm specializing in the protection of financial services professionals, executives and their families. We manage engagements resulting from general and specific threats throughout the United States and abroad on behalf of our domestic clients. We deliver our services exclusively through associates and contractors with United States special operations, secret service, CIA, or equivalent experience and training. We are one of only a handful of domestic security firms that offers scalable, tier one security services in every market in the United States.</p>

<section class="abs testimonial"></section>
<div class="abs t-photo" role="img" aria-label="Portrait photo of the reviewer"></div>
<div class="abs t-quote">&ldquo;</div>
<p class="abs t-text">Lorem ipsum dolor sit amet, consectetuer adipiscing elit, sed diam nonummy nibh euismod tincidunt ut laoreet dolore magna aliquam erat volutpat. Ut wisi enim ad minim veniam, quis nostrud exerci tation ullamcorper suscipit lobortis nisl ut aliquip ex ea commodo consequat. Duis autem vel eum iriure dolor in hendrerit in vulputate velit esse molestie consequat, vel illum dolore eu feugiat nulla facilisis.</p>
<div class="abs t-author">- Lorem Ipsum</div>
<div class="abs t-more">Read More</div>

<section class="abs services-bg"></section>
<h2 class="abs heading sec-title" style="left:98px;top:1545px">Service Offerings</h2>
<div class="abs divider" style="left:98px;top:1608px;width:619px"></div>
<h2 class="abs heading sec-title" style="left:794px;top:1545px">Contact Us Form</h2>
<div class="abs divider" style="left:794px;top:1608px;width:298px"></div>

<div class="abs svc-icon" style="left:100px;top:1644px"><svg width="54" height="54" viewBox="0 0 54 54" fill="none" stroke="#fff" stroke-width="4"><circle cx="27" cy="27" r="22"/><circle cx="27" cy="27" r="12"/><circle cx="27" cy="27" r="3" fill="#fff"/></svg></div>
<div class="abs svc-name" style="left:222px;top:1650px">Threat Assessment</div>
<p class="abs svc-desc" style="left:222px;top:1676px">Donec et lorem quis erat commodo suscipit. Mae elit a, eleifend leo.</p>

<div class="abs svc-icon" style="left:463px;top:1644px"><svg width="54" height="54" viewBox="0 0 54 54" fill="none" stroke="#fff" stroke-width="4"><circle cx="27" cy="30" r="20"/><path d="M27 18v12l8 6M21 6h12"/></svg></div>
<div class="abs svc-name" style="left:585px;top:1650px">Threat Avoidance Plan</div>
<p class="abs svc-desc" style="left:585px;top:1676px">Donec et lorem quis erat commodo suscipit. Mae elit a, eleifend leo.</p>

<div class="abs svc-icon" style="left:100px;top:1798px"><svg width="60" height="50" viewBox="0 0 60 50" fill="#fff"><circle cx="30" cy="14" r="8"/><path d="M16 44c0-10 6-16 14-16s14 6 14 16z"/><circle cx="11" cy="18" r="6"/><path d="M0 42c0-8 5-12 11-12 3 0 5 1 7 2-3 3-4 6-4 10z"/><circle cx="49" cy="18" r="6"/><path d="M60 42c0-8-5-12-11-12-3 0-5 1-7 2 3 3 4 6 4 10z"/></svg></div>
<div class="abs svc-name" style="left:222px;top:1804px">Elite Executive Protection</div>
<p class="abs svc-desc" style="left:222px;top:1830px">Donec et lorem quis erat commodo suscipit. Mae elit a, eleifend leo.</p>

<div class="abs svc-icon" style="left:463px;top:1798px"><svg width="54" height="54" viewBox="0 0 54 54" fill="none" stroke="#fff" stroke-width="4"><rect x="12" y="6" width="30" height="40" rx="3"/><path d="M19 18h16M19 26h16M19 34h10"/></svg></div>
<div class="abs svc-name" style="left:585px;top:1804px">Dossier Maintenance</div>
<p class="abs svc-desc" style="left:585px;top:1830px">Donec et lorem quis erat commodo suscipit. Mae elit a, eleifend leo.</p>

<div class="abs svc-icon" style="left:100px;top:1952px"><svg width="54" height="54" viewBox="0 0 54 54" fill="none" stroke="#fff" stroke-width="4"><circle cx="27" cy="27" r="22"/><circle cx="27" cy="27" r="12"/><circle cx="27" cy="27" r="3" fill="#fff"/></svg></div>
<div class="abs svc-name" style="left:222px;top:1958px">Threat Assessment</div>
<p class="abs svc-desc" style="left:222px;top:1984px">Donec et lorem quis erat commodo suscipit. Mae elit a, eleifend leo.</p>

<div class="abs svc-icon" style="left:463px;top:1952px"><svg width="54" height="54" viewBox="0 0 54 54" fill="none" stroke="#fff" stroke-width="4"><circle cx="27" cy="30" r="20"/><path d="M27 18v12l8 6M21 6h12"/></svg></div>
<div class="abs svc-name" style="left:585px;top:1958px">Threat Avoidance Plan</div>
<p class="abs svc-desc" style="left:585px;top:1984px">Donec et lorem quis erat commodo suscipit. Mae elit a, eleifend leo.</p>

<div class="abs svc-icon" style="left:100px;top:2106px"><svg width="60" height="50" viewBox="0 0 60 50" fill="#fff"><circle cx="30" cy="14" r="8"/><path d="M16 44c0-10 6-16 14-16s14 6 14 16z"/><circle cx="11" cy="18" r="6"/><path d="M0 42c0-8 5-12 11-12 3 0 5 1 7 2-3 3-4 6-4 10z"/><circle cx="49" cy="18" r="6"/><path d="M60 42c0-8-5-12-11-12-3 0-5 1-7 2 3 3 4 6 4 10z"/></svg></div>
<div class="abs svc-name" style="left:222px;top:2112px">Elite Executive Protection</div>
<p class="abs svc-desc" style="left:222px;top:2138px">Donec et lorem quis erat commodo suscipit. Mae elit a, eleifend leo.</p>

<div class="abs svc-icon" style="left:463px;top:2106px"><svg width="54" height="54" viewBox="0 0 54 54" fill="none" stroke="#fff" stroke-width="4"><rect x="12" y="6" width="30" height="40" rx="3"/><path d="M19 18h16M19 26h16M19 34h10"/></svg></div>
<div class="abs svc-name" style="left:585px;top:2112px">Dossier Maintenance</div>
<p class="abs svc-desc" style="left:585px;top:2138px">Donec et lorem quis erat commodo suscipit. Mae elit a, eleifend leo.</p>

<div class="abs form-panel"></div>
<div class="abs field" style="top:1668px">First Name</div>
<div class="abs field" style="top:1717px">Last Name</div>
<div class="abs field" style="top:1766px">Home Phone</div>
<div class="abs field" style="top:1815px">Work Phone</div>
<div class="abs field" style="top:1864px">Cell Phone</div>
<div class="abs field" style="top:1913px">Email Address</div>
<div class="abs field" style="top:1962px">City</div>
<div class="abs field" style="top:2011px">State</div>
<div class="abs field" style="top:2060px">Zip</div>
<div class="abs field" style="top:2106px;height:80px">Message</div>
<div class="abs send">Send</div>

<section class="abs footer-dark"></section>
<div class="abs f-title" style="left:117px;top:2328px">PEOPLE REVIEWS</div>
<div class="abs f-rule" style="left:117px;top:2374px;width:290px"></div>
<p class="abs review">Lorem ipsum dolor sit amet, consectetuer adipiscing elit, sed diam nonummy nibh euismod tincidunt ut laoreet dolore magna aliquam erat volutpat. Ut wisi enim ad minim veniam, quis nostrud exerci tation ullamcorper suscipit lobortis nisl ut aliquip ex ea commodo consequat. Duis autem vel eum iriure dolor in hendrerit in vulputate velit esse molestie consequat, vel illum dolore eu feugiat nulla facilisis.</p>
<div class="abs review-name">Lorem Ipsum<br>CEO, USA</div>
<div class="abs pager" style="left:356px;width:22px;background:#fff"></div>
<div class="abs pager" style="left:382px;width:14px"></div>

<div class="abs f-title" style="left:483px;top:2328px">FLICKER FEED</div>
<div class="abs f-rule" style="left:483px;top:2374px;width:259px"></div>
<div class="abs thumb" style="left:483px;top:2394px" role="img" aria-label="Photo of a businessman"></div>
<div class="abs thumb" style="left:618px;top:2394px" role="img" aria-label="Photo of a businessman"></div>
<div class="abs thumb" style="left:483px;top:2524px" role="img" aria-label="Photo of a businesswoman"></div>
<div class="abs thumb" style="left:618px;top:2524px" role="img" aria-label="Photo of a businesswoman"></div>

<div class="abs f-title" style="left:815px;top:2328px">NEWS LETTER</div>
<div class="abs f-rule" style="left:815px;top:2374px;width:262px"></div>
<div class="abs news-box"></div>
<p class="abs news-text">Quisque volutpat mattis eros. Nullam malesuada erat ut turpis. Suspendisse.</p>
<div class="abs news-input">Email</div>
<div class="abs news-btn">SUBMIT</div>

<footer class="abs footer-bar">
  <span class="abs" style="left:98px;top:18px">Copyright &copy; 2014 Marlowvex All Reserved. Designed &amp; Developed By PixelForge Studio</span>
  <span class="abs" style="left:728px;top:18px">Company Description &nbsp;/&nbsp; Service Offerings &nbsp;/&nbsp; Contact Us</span>
</footer>

</body>
</html>
```